Interior Design/ decoration business card design

This card is for my Interior Design and Decoration business and later I will also be selling homewares. I would like the card to be very simple in design and like either white, duck egg blue , aquas or metallics on a flat mat card excellent quality card. It needs to be well designed as that is my field. I dont like fuss, the simpler the better. I would like a styalised wren under the name wren if possible. SIMPLE, STYLISH, CLASSIC, TASTEFUL

Target Market(s)

40 + year olds who are building or rennovating.

Industry/Entity Type

Business

Contact Information for Business Card

Wren
styling, design, homeware

Marnie Tolland
p 0427316958
e marnie@wrenliving.com.au
w wrenliving.com.au

Requirements
Must have
• very simple, stylish, classic, sophisticated. Simple and easy to read text that is a print similar to attached image. I like simple round A's though not as in attached image.

Double sided. It wont save as double sided for some reason!!
Should not have
• not too much colour, No animated / cartoon pictures.

```html
<!DOCTYPE html>
<html lang="en">
<head>
<meta charset="utf-8">
<title>Wren — business card</title>
<link href="https://fonts.googleapis.com/css2?family=Questrial&family=Mulish:wght@400;700&display=swap" rel="stylesheet">
<style>
  :root {
    --backdrop: #e9e8e6;
    --card-white: #ffffff;
    --duck-egg: #b9d9d5;
    --ink: #4a4947;
    --ink-soft: #5d5b58;
    --name-white: #ffffff;
  }
  * { margin: 0; padding: 0; box-sizing: border-box; }
  html, body {
    width: 1200px; height: 583px; overflow: hidden;
    background: var(--backdrop);
  }
  .stage {
    position: relative; width: 1200px; height: 583px;
    display: flex; align-items: center; justify-content: center; gap: 50px;
  }
  .card {
    position: relative; width: 525px; height: 300px;
    background: var(--card-white); overflow: hidden;
    box-shadow: 0 4px 14px rgba(0,0,0,0.12);
  }

  /* Contact side */
  .contact-side .lower-band {
    position: absolute; left: 0; right: 0; top: 148px; bottom: 0;
    background: var(--duck-egg);
  }
  .contact-side .notch {
    position: absolute; top: 147px; left: 408px;
    width: 0; height: 0;
    border-left: 9px solid transparent; border-right: 9px solid transparent;
    border-top: 9px solid var(--card-white);
  }
  .contact-side .brand {
    position: absolute; right: 32px; top: 30px; text-align: right;
  }
  .wordmark {
    font-family: "Questrial", sans-serif; color: var(--ink); line-height: 1;
  }
  .contact-side .wordmark { font-size: 34px; margin-right: 78px; }
  .tagline {
    font-family: "Questrial", sans-serif; color: var(--ink-soft); white-space: nowrap;
  }
  .tagline .bar { display: inline-block; width: 1.5px; height: 1em; background: var(--ink); vertical-align: -2px; margin: 0 3px; }
  .contact-side .tagline { font-size: 12.5px; margin-top: 36px; }
  .holder {
    position: absolute; right: 32px; top: 166px; text-align: right;
    font-family: "Mulish", sans-serif;
  }
  .holder .name { color: var(--name-white); font-weight: 700; font-size: 14px; letter-spacing: 0.3px; }
  .holder .role { color: var(--ink); font-size: 13px; margin-top: 2px; }
  .details {
    position: absolute; left: 42px; bottom: 26px; list-style: none;
    font-family: "Mulish", sans-serif; font-weight: 700; font-size: 12.5px; color: var(--ink);
  }
  .details li { display: flex; align-items: center; gap: 10px; height: 24px; }
  .details svg { width: 14px; height: 14px; flex: none; }

  /* Brand side */
  .brand-side .top-band { position: absolute; left: 0; right: 0; top: 0; height: 46px; background: var(--duck-egg); }
  .brand-side .bottom-band { position: absolute; left: 0; right: 0; bottom: 0; height: 92px; background: var(--duck-egg); }
  .brand-side .brand { position: absolute; left: 0; right: 0; top: 76px; text-align: center; }
  .brand-side .wordmark { font-size: 48px; margin-left: 20px; }
  .brand-side .tagline { font-size: 17px; margin-top: 34px; }
</style>
</head>
<body>
<main class="stage">
  <section class="card contact-side" aria-label="Card back with contact details">
    <div class="lower-band"></div>
    <div class="notch"></div>
    <div class="brand">
      <div class="wordmark">wren</div>
      <div class="tagline">decoration<span class="bar"></span>styling<span class="bar"></span>homeware</div>
    </div>
    <div class="holder">
      <div class="name">Marnie Tolland</div>
      <div class="role">Homeware Expert</div>
    </div>
    <ul class="details">
      <li>
        <svg viewBox="0 0 14 14" aria-hidden="true"><rect x="0.5" y="0.5" width="13" height="13" rx="2" fill="#fff" opacity="0.85"/><rect x="4.5" y="2.5" width="5" height="9" rx="1" fill="none" stroke="#4a4947"/></svg>
        0427316958
      </li>
      <li>
        <svg viewBox="0 0 14 14" aria-hidden="true"><rect x="0.5" y="0.5" width="13" height="13" rx="2" fill="#fff" opacity="0.85"/><rect x="2.5" y="4" width="9" height="6" fill="none" stroke="#4a4947"/><path d="M2.5 4 7 7.5 11.5 4" fill="none" stroke="#4a4947"/></svg>
        marnie@wrenliving.com.au
      </li>
      <li>
        <svg viewBox="0 0 14 14" aria-hidden="true"><rect x="0.5" y="0.5" width="13" height="13" rx="2" fill="#fff" opacity="0.85"/><circle cx="7" cy="7" r="4" fill="none" stroke="#4a4947"/><path d="M3 7h8M7 3c-2 2.5-2 5.5 0 8M7 3c2 2.5 2 5.5 0 8" fill="none" stroke="#4a4947" stroke-width="0.8"/></svg>
        wrenliving.com.au
      </li>
    </ul>
  </section>

  <section class="card brand-side" aria-label="Card front with brand name">
    <div class="top-band"></div>
    <div class="bottom-band"></div>
    <div class="brand">
      <div class="wordmark">wren</div>
      <div class="tagline">decoration<span class="bar"></span>styling<span class="bar"></span>homeware</div>
    </div>
  </section>
</main>
</body>
</html>
```